Business card and stationary for consulting business

We need business cards and matching stationary for professional consulting business for employment and human resources issues.
One of the PixelHarbor designers designed the logo with our company name.  Use the colors in the logo and may use light yellow as an accent color.
Add
Nora T. Vandell, J.D., LL.M.
485 E. Corliss Road
Winter Park, Florida  32814
407-555-0182
noravandelljd@mailbrook.net

```html
<!DOCTYPE html>
<html lang="en">
<head>
<meta charset="utf-8">
<title>Clearway Consulting — Business Card</title>
<link href="https://fonts.googleapis.com/css2?family=Quicksand:wght@400;500;600&display=swap" rel="stylesheet">
<style>
  :root {
    --brand-blue: #1f77a3;
    --brand-dark: #1a6590;
    --paper: #ffffff;
    --backdrop: #e9edf0;
    --card-shadow: rgba(20, 45, 60, 0.18);
  }
  * { box-sizing: border-box; margin: 0; padding: 0; }
  html, body {
    width: 1200px;
    height: 900px;
    overflow: hidden;
    background: var(--backdrop);
    font-family: "Quicksand", sans-serif;
  }
  .canvas {
    position: relative;
    width: 1200px;
    height: 900px;
  }
  .card {
    position: absolute;
    left: 285px;
    width: 630px;
    height: 360px;
    background: var(--paper);
    box-shadow: 0 10px 28px var(--card-shadow);
    overflow: hidden;
  }
  .card--front { top: 60px; }
  .card--back  { top: 480px; }

  /* Front */
  .front__band {
    position: absolute;
    left: 0; right: 0; bottom: 0;
    height: 208px;
    background: var(--brand-blue);
    box-shadow: 0 -4px 10px rgba(0,0,0,0.12);
  }
  .front__first-name {
    position: absolute;
    left: 18px; top: 108px;
    font-size: 34px;
    font-weight: 500;
    color: var(--brand-blue);
    line-height: 1;
  }
  .front__surname {
    position: absolute;
    left: 88px; top: 160px;
    font-size: 30px;
    font-weight: 500;
    color: var(--paper);
    line-height: 1;
  }

  .brand {
    position: absolute;
    display: flex;
    align-items: center;
    gap: 12px;
  }
  .brand__mark {
    width: 14px;
    height: 14px;
    background: var(--brand-dark);
    flex: none;
  }
  .brand__name {
    font-weight: 500;
    color: var(--brand-dark);
    white-space: nowrap;
    line-height: 1;
  }
  .card--front .brand { top: 66px; right: 28px; }
  .card--front .brand__name { font-size: 30px; }

  .contact {
    position: absolute;
    left: 380px; top: 226px;
    list-style: none;
    color: var(--paper);
    font-size: 13.5px;
    line-height: 1.35;
  }
  .contact__item {
    display: flex;
    align-items: flex-start;
    margin-bottom: 12px;
  }
  .contact__icon {
    width: 16px; height: 16px;
    margin-right: 12px;
    flex: none;
    margin-top: 1px;
  }

  /* Back */
  .back__tab {
    position: absolute;
    left: 0; top: 0;
    width: 88px; height: 92px;
    background: var(--brand-blue);
  }
  .back__block {
    position: absolute;
    right: 0; bottom: 0;
    width: 200px; height: 120px;
    background: var(--brand-blue);
    box-shadow: -4px -4px 10px rgba(0,0,0,0.1);
  }
  .card--back .brand { top: 134px; left: 120px; }
  .card--back .brand__mark { width: 18px; height: 18px; }
  .card--back .brand__name { font-size: 42px; }
</style>
</head>
<body>
<main class="canvas">

  <section class="card card--front" aria-label="Business card front">
    <div class="front__band"></div>
    <p class="front__first-name">Nora</p>
    <p class="front__surname">T. Vandell, J.D., LL.M.</p>

    <div class="brand">
      <span class="brand__mark"></span>
      <span class="brand__name">Clearway Consulting</span>
    </div>

    <ul class="contact">
      <li class="contact__item">
        <svg class="contact__icon" viewBox="0 0 16 16" aria-hidden="true">
          <rect x="4" y="1" width="8" height="14" rx="1.5" fill="none" stroke="#fff" stroke-width="1.4"/>
          <rect x="5.5" y="3" width="5" height="6" fill="#fff"/>
          <circle cx="8" cy="12.3" r="0.9" fill="#fff"/>
        </svg>
        <span>407-555-0182</span>
      </li>
      <li class="contact__item">
        <svg class="contact__icon" viewBox="0 0 16 16" aria-hidden="true">
          <path d="M8 1a4.5 4.5 0 0 0-4.5 4.5C3.5 9 8 15 8 15s4.5-6 4.5-9.5A4.5 4.5 0 0 0 8 1z" fill="#fff"/>
          <circle cx="8" cy="5.5" r="1.7" fill="#1f77a3"/>
        </svg>
        <span>485 E. Corliss Road<br>Winter Park, Florida 32814</span>
      </li>
      <li class="contact__item">
        <svg class="contact__icon" viewBox="0 0 16 16" aria-hidden="true">
          <rect x="1" y="3.5" width="14" height="9.5" fill="none" stroke="#fff" stroke-width="1.4"/>
          <path d="M1 3.5 8 9l7-5.5" fill="none" stroke="#fff" stroke-width="1.4"/>
        </svg>
        <span>noravandelljd@mailbrook.net</span>
      </li>
    </ul>
  </section>

  <section class="card card--back" aria-label="Business card back">
    <div class="back__tab"></div>
    <div class="back__block"></div>
    <div class="brand">
      <span class="brand__mark"></span>
      <span class="brand__name">Clearway Consulting</span>
    </div>
  </section>

</main>
</body>
</html>
```